Energy Company needs a Business Card Design

We need a business card design for a new company based in Singapore called Tarn Energy. Tarn Energy is a producer of renewable energies largely for the biofuels market. Sourced entirely from sustainable resources, Tarn Energy aims to be a fully integrated oil company operating in 100% sustainable way. We would like to see designs that use the same colours as the attached file.

Industry/Entity Type

Business

```html
<!DOCTYPE html>
<html lang="en">
<head>
<meta charset="utf-8">
<title>Tarn Energy – Business Card</title>
<link rel="stylesheet" href="https://fonts.googleapis.com/css2?family=Roboto:ital,wght@0,400;0,500;1,400&display=swap">
<style>
  :root {
    --stage: #a3a4a3;
    --card: #ffffff;
    --card-back: #f4f4f3;
    --green: #8cbf2f;
    --mark-grey: #c4c4c4;
    --wave-grey: #c9c9c9;
    --ink: #555657;
    --icon: #6e6f70;
  }
  * { margin: 0; padding: 0; box-sizing: border-box; }
  html, body { width: 1200px; height: 1080px; overflow: hidden; }
  body {
    background: var(--stage);
    font-family: "Roboto", Arial, sans-serif;
    position: relative;
  }
  .card {
    position: absolute;
    top: 120px;
    width: 480px;
    height: 839px;
    overflow: hidden;
  }
  .card--front { left: 91px; background: var(--card); }
  .card--back {
    left: 634px;
    background: radial-gradient(circle at 40% 35%, #fafafa 0%, var(--card-back) 70%);
  }
  .side-bar {
    position: absolute;
    top: 17px;
    width: 19px;
    height: 244px;
    background: var(--green);
  }
  .side-bar--left { left: 0; }
  .side-bar--right { right: 0; }
  .wordmark {
    position: absolute;
    left: 0; right: 0;
    display: flex;
    align-items: center;
    justify-content: center;
    gap: 14px;
  }
  .wordmark__dot {
    width: 22px; height: 22px;
    border-radius: 50%;
    background: var(--green);
  }
  .wordmark__name {
    font-weight: 500;
    font-size: 58px;
    color: var(--mark-grey);
    letter-spacing: 0.5px;
    white-space: nowrap;
  }
  .card--front .wordmark { top: 110px; }
  .card--back .wordmark { top: 318px; }
  .holder-name {
    position: absolute;
    top: 306px; left: 0; right: 0;
    text-align: center;
    font-size: 33px;
    color: var(--ink);
    letter-spacing: 1px;
  }
  .holder-role {
    position: absolute;
    top: 346px; left: 0; right: 0;
    display: flex;
    align-items: center;
    gap: 10px;
  }
  .holder-role::before, .holder-role::after {
    content: "";
    flex: 1;
    height: 4px;
    background: var(--green);
  }
  .holder-role span { font-size: 22px; color: var(--ink); }
  .contacts {
    position: absolute;
    top: 426px; left: 122px;
    list-style: none;
  }
  .contacts li {
    display: flex;
    align-items: center;
    height: 52.5px;
    font-size: 26px;
    color: var(--ink);
    letter-spacing: 0.5px;
  }
  .contacts svg { width: 28px; height: 30px; margin-right: 14px; fill: var(--icon); }
  .wave { position: absolute; left: 0; bottom: 0; width: 480px; height: 180px; }
  .slogan {
    position: absolute;
    top: 548px; left: 0; right: 0;
    text-align: center;
    font-style: italic;
    font-size: 30px;
    color: var(--green);
  }
</style>
</head>
<body>
  <section class="card card--front" aria-label="Business card front">
    <div class="side-bar side-bar--left"></div>
    <div class="side-bar side-bar--right"></div>
    <div class="wordmark"><span class="wordmark__dot"></span><span class="wordmark__name">Tarn Energy</span></div>
    <h1 class="holder-name">XXXXXXXXXXXXX</h1>
    <p class="holder-role"><span>Managing Director</span></p>
    <ul class="contacts">
      <li><svg viewBox="0 0 24 24"><path d="M12 2a7 7 0 0 0-7 7c0 5 7 13 7 13s7-8 7-13a7 7 0 0 0-7-7zm0 9.5A2.5 2.5 0 1 1 12 6.5a2.5 2.5 0 0 1 0 5z"/></svg>XXXXXXXXXXXX</li>
      <li><svg viewBox="0 0 24 24"><path d="M6.6 10.8a15 15 0 0 0 6.6 6.6l2.2-2.2c.3-.3.7-.4 1-.2 1.1.4 2.3.6 3.6.6.6 0 1 .4 1 1V20c0 .6-.4 1-1 1A17 17 0 0 1 3 4c0-.6.4-1 1-1h3.5c.6 0 1 .4 1 1 0 1.3.2 2.5.6 3.6.1.3 0 .7-.2 1z"/></svg>XXXXXXXXXXXX</li>
      <li><svg viewBox="0 0 24 24"><path d="M8 1h8a2 2 0 0 1 2 2v18a2 2 0 0 1-2 2H8a2 2 0 0 1-2-2V3a2 2 0 0 1 2-2zm0 3v14h8V4zm4 15.5a1 1 0 1 0 0 2 1 1 0 0 0 0-2z"/></svg>XXXXXXXXXXXX</li>
      <li><svg viewBox="0 0 24 24"><path d="M12 2a10 10 0 1 0 0 20 10 10 0 0 0 0-20zm6.9 6h-3a15 15 0 0 0-1.3-3.9A8 8 0 0 1 18.9 8zM12 4c.8 1.2 1.5 2.5 1.9 4h-3.8c.4-1.5 1.1-2.8 1.9-4zM4.3 14a8 8 0 0 1 0-4h3.4a16 16 0 0 0 0 4zm.8 2h3a15 15 0 0 0 1.3 3.9A8 8 0 0 1 5.1 16zm3-8h-3a8 8 0 0 1 4.3-3.9C8.8 5.3 8.4 6.6 8.1 8zM12 20c-.8-1.2-1.5-2.5-1.9-4h3.8c-.4 1.5-1.1 2.8-1.9 4zm2.3-6H9.7a14 14 0 0 1 0-4h4.6a14 14 0 0 1 0 4zm.3 5.9c.6-1.2 1-2.5 1.3-3.9h3a8 8 0 0 1-4.3 3.9zM16.3 14a16 16 0 0 0 0-4h3.4a8 8 0 0 1 0 4z"/></svg>XXXXXXXXXXXX</li>
      <li><svg viewBox="0 0 24 24"><path d="M2 5h20v14H2zm2 2v.5l8 5.5 8-5.5V7zm0 2.9V17h16V9.9l-8 5.5z"/></svg>XXXXXXXXXXXX</li>
    </ul>
    <svg class="wave" viewBox="0 0 480 180" aria-hidden="true">
      <path fill="var(--wave-grey)" d="M0 50 C110 20 210 55 300 40 C380 26 440 6 480 0 L480 180 L0 180 Z"/>
      <path fill="#ffffff" d="M0 58 C110 30 210 64 300 50 C380 37 440 18 480 12 L480 180 L0 180 Z"/>
      <path fill="var(--green)" d="M0 74 C110 48 210 80 300 66 C380 54 440 36 480 30 L480 180 L0 180 Z"/>
    </svg>
  </section>

  <section class="card card--back" aria-label="Business card back">
    <div class="wordmark"><span class="wordmark__dot"></span><span class="wordmark__name">Tarn Energy</span></div>
    <p class="slogan">“xxxxx Slogan xxxxx”</p>
  </section>
</body>
</html>
```